Gentle threads

Organic ethical yoga/activewear that supports kids in need and other community projects by donating % of all sales to these causes. See the product and the brand (Wirra project) story and catalogue on
Gentlethreads.com.au
http://files.palmbrook.net/doc/k7rq2m_a41c93e7b20d4f58c61e8a9d3f027b6e.pdf
Flyer is for gentle threads as the distributor for Wirra clothing
Would like the flyer to be simple with core message and contact and site details but have a similar feel to the catalogue using some of the art graphics and or photo from site for colour. Also for wholesale/distributor enquiries or to arrange an appointment for a brand presentation contact Mara Lodge 0412
Updates
I have four that I am considering so please don't submit any more. One of these will be suitable. Thanks for your submissions.
Mara
Target Market(s)
Yoga studios, wellness centres , private parties, gyms, agents
Industry/Entity Type
Clothing
Look and feel
Each slider illustrates characteristics of the customer's brand and the style your logo design should communicate.

```html
<!DOCTYPE html>
<html lang="en">
<head>
<meta charset="utf-8">
<title>Gentle Threads – Flyer</title>
<link rel="stylesheet" href="https://fonts.googleapis.com/css2?family=Amatic+SC:wght@400;700&display=swap">
<style>
  :root{
    --page-bg:#e6e0e4;
    --paper:#fbfafb;
    --paper-tint:#f1ecf1;
    --ink:#1f1f1f;
    --band:#1c1c1c;
    --band-text:#f5f5f5;
    --tile-mint:#7fc3b5;
    --tile-navy:#3d4a8a;
    --tile-charcoal:#3b3c3e;
    --tile-lilac:#caa9c6;
    --tile-black:#2a2c2d;
    --tile-grey:#7c7e83;
    --tile-violet:#6d6fab;
  }
  *{margin:0;padding:0;box-sizing:border-box}
  html,body{width:1200px;height:1000px;overflow:hidden;background:var(--page-bg)}
  body{position:relative;font-family:"Amatic SC",cursive}
  .flyer{
    position:absolute;left:270px;top:31px;width:660px;height:938px;
    background:var(--paper);overflow:hidden;
  }
  .flyer-pattern{
    position:absolute;inset:0;
    background:linear-gradient(180deg,var(--paper) 0%,var(--paper-tint) 50%,var(--paper) 100%);
  }
  .flyer-title{
    position:absolute;top:18px;left:0;width:100%;text-align:center;
    font-weight:700;font-size:60px;line-height:1;color:var(--ink);letter-spacing:1px;
  }
  .zigzag{position:absolute;left:246px;width:168px;height:8px}
  .zigzag-top{top:100px}
  .zigzag-bottom{top:842px}
  .collage{position:absolute;left:0;top:0;width:660px;height:720px}
  .tagline{
    position:absolute;left:142px;top:735px;width:380px;height:80px;
    background:var(--band);color:var(--band-text);
    display:flex;flex-direction:column;justify-content:center;align-items:center;
    font-size:25px;line-height:1.05;text-align:center;
  }
  .contact{
    position:absolute;top:872px;left:0;width:100%;height:40px;
    color:var(--ink);font-weight:700;
  }
  .contact-lead{position:absolute;left:24px;top:4px;font-size:21px;white-space:nowrap}
  .contact-office,.contact-web{position:absolute;top:0;font-size:16px;line-height:1.15;white-space:nowrap}
  .contact-office{left:346px}
  .contact-web{left:476px}
</style>
</head>
<body>
  <main class="flyer">
    <div class="flyer-pattern" role="img" aria-label="Soft pastel tribal geometric pattern background"></div>

    <h1 class="flyer-title">Gentle Threads</h1>
    <svg class="zigzag zigzag-top" viewBox="0 0 168 8" aria-hidden="true">
      <polyline points="0,6 4,2 8,6 12,2 16,6 20,2 24,6 28,2 32,6 36,2 40,6 44,2 48,6 52,2 56,6 60,2 64,6 68,2 72,6 76,2 80,6 84,2 88,6 92,2 96,6 100,2 104,6 108,2 112,6 116,2 120,6 124,2 128,6 132,2 136,6 140,2 144,6 148,2 152,6 156,2 160,6 164,2 168,6" fill="none" stroke="#1f1f1f" stroke-width="1.4"/>
    </svg>

    <svg class="collage" viewBox="0 0 660 720">
      <polygon role="img" aria-label="Photo: mint patterned top" fill="var(--tile-mint)" points="331,128 424,221 331,314 238,221"/>
      <polygon role="img" aria-label="Photo: blue printed activewear" fill="var(--tile-navy)" points="234,225 327,318 234,411 141,318"/>
      <polygon role="img" aria-label="Photo: black geometric singlet" fill="var(--tile-charcoal)" points="428,225 521,318 428,411 335,318"/>
      <polygon role="img" aria-label="Photo: brand banner held at a community project" fill="var(--tile-lilac)" points="331,353 393,415 331,477 269,415"/>
      <polygon role="img" aria-label="Photo: black printed t-shirt" fill="var(--tile-black)" points="234,419 327,512 234,605 141,512"/>
      <polygon role="img" aria-label="Photo: grey hooded top" fill="var(--tile-grey)" points="428,419 521,512 428,605 335,512"/>
      <polygon role="img" aria-label="Artwork: purple and teal geometric print" fill="var(--tile-violet)" points="331,516 424,609 331,702 238,609"/>
    </svg>

    <div class="tagline">
      <span>Ethical, conscious and organic products</span>
      <span>supporting the community</span>
    </div>

    <svg class="zigzag zigzag-bottom" viewBox="0 0 168 8" aria-hidden="true">
      <polyline points="0,6 4,2 8,6 12,2 16,6 20,2 24,6 28,2 32,6 36,2 40,6 44,2 48,6 52,2 56,6 60,2 64,6 68,2 72,6 76,2 80,6 84,2 88,6 92,2 96,6 100,2 104,6 108,2 112,6 116,2 120,6 124,2 128,6 132,2 136,6 140,2 144,6 148,2 152,6 156,2 160,6 164,2 168,6" fill="none" stroke="#1f1f1f" stroke-width="1.4"/>
    </svg>

    <footer class="contact">
      <p class="contact-lead">For wholesale/distributor enquiries contact:</p>
      <p class="contact-office">Head Office - Mara Lodge<br>Tel: 0412 538 61</p>
      <p class="contact-web">Gentlethreads.com.au<br>info@gentlethreads.com.au</p>
    </footer>
  </main>
</body>
</html>
```